Roofing Company needs YOU to help put us on top!

Brightpeak Roofing, a fresh new company with quality and Innovation in mind, needs your help to stand out in the competitive Chicago market. With over 30 years of experience, all the right people and tools for the job, the only thing we are missing is your creative ideas in web design to help us grow our online presence.
Our Company offers exceptional quality at reasonable prices, we work for the everyday people both blue collar and white collar.

We have used Craftswarm in the past with multiple successful campaigns, we are excited to see what you can come up with for our website.

www.BrightpeakRoofing.example will be the domain

We will be hiring a photographer for visual content on our pages later. Stock photos are okay to use but should follow theme.

Thank you for taking the time on the submissions, if you have any questions don't hesitate to ask and we will provide whatever is needed to you.

Target Market(s)

Homeowners & Commercial Clients between 21-65

Industry/Entity Type

Roofing

Coding

Coded - Design and coding required

Number of Pages Required

4 page

Font styles to use
Sans Serif

Colors
ffffff
ec1f27
000000
5c5c5c
757575
b2b2b2

Requirements
Must have
• Color Scheme - should follow around our logo
• As for pages we were looking for an About, Services, Projects (gallery page) and Contact.
• Main page please include social media links and a a place so people could use tillbee to make payments
• Website should work on desktop as well as mobile platforms
Nice to have
• A Live chat feature would be nice if possible
Should not have
• Obscure Colors or Common web templates

```html
<!DOCTYPE html>
<html lang="en">
<head>
<meta charset="utf-8">
<title>Brightpeak Roofing – Our Projects</title>
<link rel="stylesheet" href="https://fonts.googleapis.com/css2?family=Roboto:wght@400;500;700&display=swap">
<style>
:root{
  --red:#e3262c;
  --red-soft:#f0454a;
  --black:#141414;
  --white:#ffffff;
  --ink:#2a2a2a;
  --grey:#5c5c5c;
  --grey-mid:#757575;
  --grey-light:#b2b2b2;
  --box:#2a2a2a;
}
*{margin:0;padding:0;box-sizing:border-box}
html,body{width:1185px;height:1200px;overflow:hidden;background:var(--white)}
body{position:relative;font-family:'Roboto',sans-serif;color:var(--ink)}
a{color:inherit;text-decoration:none}
.abs{position:absolute}

/* top bar */
.topbar{left:0;top:0;width:1185px;height:36px;background:var(--black);color:var(--white);font-size:12px}
.topbar .contact-item{top:11px;display:flex;align-items:center;gap:8px}
.topbar .divider{left:202px;top:9px;width:1px;height:18px;background:#3a3a3a}
.social{display:flex;gap:3px}
.social span{width:28px;height:28px;background:var(--box);display:flex;align-items:center;justify-content:center;font-size:9px;font-weight:500;color:var(--white);letter-spacing:.2px}
.topbar .social{left:977px;top:4px}

/* header */
.header{left:0;top:36px;width:1185px;height:78px;background:var(--white)}
.brand{display:flex;align-items:center;gap:6px;font-weight:700;letter-spacing:.3px}
.header .brand{left:88px;top:27px;font-size:18px;color:var(--black)}
.brand .mark{width:14px;height:14px;background:var(--red)}
.nav a{position:absolute;top:34px;font-size:13.5px;color:var(--ink)}
.nav a.active{color:var(--red)}
.nav .pointer{left:981px;top:0;width:0;height:0;border-left:8px solid transparent;border-right:8px solid transparent;border-top:7px solid var(--red)}

/* hero */
.hero{left:0;top:114px;width:1185px;height:140px;background:linear-gradient(90deg,#b9a797 0%,#c6b19f 35%,#d6c2b0 58%,#5a4a40 70%,#3a302a 82%,#c3ad99 95%,#b7a08c 100%)}
.hero-title{left:0;width:1185px;top:44px;text-align:center;color:var(--white);font-size:33px;font-weight:400}
.crumb{left:0;width:1185px;top:85px;display:flex;justify-content:center;align-items:center;gap:7px;color:var(--white);font-size:14px}

/* gallery */
.tile{width:248px;height:202px}
.t1{background:linear-gradient(135deg,#1e2530 0%,#e4e6ea 18%,#c8ccd4 45%,#7d8799 70%,#3f4a5e 100%)}
.t2{background:linear-gradient(180deg,#4b98e6 0%,#5aa7ef 30%,#8a4a38 42%,#a5503b 62%,#b4513d 80%,#8c3a2c 100%)}
.t3{background:linear-gradient(160deg,#9aa1aa 0%,#6b7077 35%,#4a4f57 65%,#30343a 100%)}
.t4{background:linear-gradient(180deg,#555756 0%,#7c7d7a 30%,#a3a39f 60%,#c0c0bb 100%)}
.t5{background:linear-gradient(170deg,#d7dce2 0%,#b8bcb4 35%,#8e8a80 55%,#a07a4c 75%,#6e5032 100%)}
.t6{background:linear-gradient(160deg,#c7d8e8 0%,#8c8a68 40%,#5d5a3c 65%,#c86a2c 85%,#4a4232 100%)}
.t7{background:linear-gradient(170deg,#1b86d8 0%,#2e9be2 35%,#e9eef0 48%,#15867a 60%,#0f6d63 75%,#3a2f2a 100%)}
.t8{background:linear-gradient(170deg,#2f4f94 0%,#4c68a8 30%,#8b7d62 50%,#aab2c2 72%,#d6dbe3 100%)}
.tile-hover{left:598px;top:319px;width:247px;height:202px}
.tile-shade{left:0;top:0;width:247px;height:160px;background:rgba(0,0,0,.22)}
.tile-caption{left:0;bottom:0;width:247px;height:42px;background:var(--red);color:var(--white);font-size:14.5px;display:flex;align-items:center;justify-content:center}
.tile-btn{top:74px;width:38px;height:38px;border-radius:50%;background:var(--white);display:flex;align-items:center;justify-content:center}

.load-more{left:535px;top:762px;width:116px;height:36px;background:var(--red);color:var(--white);font-size:12.5px;display:flex;align-items:center;justify-content:center}

/* call to action */
.cta{left:0;top:839px;width:1185px;height:89px;background:var(--red);color:var(--white)}
.cta-kicker{left:86px;top:25px;font-size:16px}
.cta-title{left:86px;top:43px;font-size:22px}
.cta-phone{left:776px;top:34px;display:flex;align-items:center;gap:9px;font-size:18px}
.cta-btn{left:927px;top:30px;width:170px;height:33px;background:var(--red-soft);color:var(--white);font-size:11px;display:flex;align-items:center;justify-content:center;letter-spacing:.2px}

/* footer */
.footer{left:0;top:928px;width:1185px;height:272px;background:var(--black);color:var(--white)}
.footer .brand{left:88px;top:62px;font-size:20px;color:var(--white)}
.footer .brand .mark{width:15px;height:15px}
.footer-phone{left:106px;top:92px;font-size:15px;font-weight:700;letter-spacing:1px}
.col-title{top:75px;font-size:18px;font-weight:400}
.links a{position:absolute;font-size:12.5px}
.info{font-size:12.5px;line-height:18px}
.info-row{display:flex;align-items:center;gap:8px;font-size:12.5px}
.footer .social{left:961px;top:68px}
.footer .social span{width:31px;height:28px}
.copyright{right:90px;top:109px;text-align:right;font-size:12.5px;line-height:19px}
.pay-badge{left:1053px;top:155px;width:44px;height:27px;background:#fff4d6;border:1px solid #e8b84a;border-radius:2px;color:#1b3a7a;font-size:9.5px;font-weight:700;display:flex;align-items:center;justify-content:center}
.chat{left:1071px;top:201px;display:flex;align-items:center;gap:8px}
.chat-bubble{width:42px;height:42px;border-radius:50%;background:var(--red);display:flex;align-items:center;justify-content:center}
.chat-label{line-height:1}
.chat-label small{display:block;font-size:12px}
.chat-label b{font-weight:400;font-size:20px}
</style>
</head>
<body>

<div class="topbar abs">
  <div class="contact-item abs" style="left:88px">
    <svg width="12" height="12" viewBox="0 0 24 24"><path fill="#fff" d="M6.6 10.8a15.1 15.1 0 0 0 6.6 6.6l2.2-2.2c.3-.3.7-.4 1-.2 1.1.4 2.3.6 3.6.6.6 0 1 .4 1 1V20c0 .6-.4 1-1 1A17 17 0 0 1 3 4c0-.6.4-1 1-1h3.5c.6 0 1 .4 1 1 0 1.3.2 2.5.6 3.6.1.3 0 .7-.2 1z"/></svg>
    555-014-0008
  </div>
  <div class="divider abs"></div>
  <div class="contact-item abs" style="left:221px">
    <svg width="12" height="10" viewBox="0 0 24 18"><rect x="1" y="1" width="22" height="16" fill="none" stroke="#fff" stroke-width="2"/><path d="M1 1l11 9 11-9" fill="none" stroke="#fff" stroke-width="2"/></svg>
    info@brightpeakroofing.example
  </div>
  <div class="social abs" aria-label="Social links"><span>pix</span><span>hum</span><span>orb</span><span>nod</span></div>
</div>

<header class="header abs">
  <div class="brand abs"><span class="mark"></span>Brightpeak Roofing</div>
  <nav class="nav">
    <span class="pointer abs"></span>
    <a style="left:736px">Home</a>
    <a style="left:808px">About</a>
    <a style="left:880px">Services</a>
    <a class="active" style="left:966px">Projects</a>
    <a style="left:1051px">Contact</a>
  </nav>
</header>

<section class="hero abs" role="img" aria-label="Roofing crew silhouettes against a warm sunset sky">
  <h1 class="hero-title abs">Our Projects</h1>
  <div class="crumb abs">
    <svg width="15" height="13" viewBox="0 0 24 20"><path fill="#fff" d="M12 1 1 10h3v9h6v-6h4v6h6v-9h3z"/></svg>
    Home / Projects
  </div>
</section>

<main>
  <div class="tile t1 abs" style="left:90px;top:319px" role="img" aria-label="Modern glass skyscraper with white steel ribs"></div>
  <div class="tile t2 abs" style="left:344px;top:319px" role="img" aria-label="Brick chimneys on a red tile roof under blue sky"></div>
  <div class="tile t3 abs tile-hover" role="img" aria-label="Workers installing roof panels">
    <div class="tile-shade abs"></div>
    <div class="tile-btn abs" style="left:81px">
      <svg width="13" height="13" viewBox="0 0 24 24"><circle cx="10" cy="10" r="7" fill="none" stroke="#222" stroke-width="2.5"/><path d="M15 15l6 6" stroke="#222" stroke-width="2.5"/></svg>
    </div>
    <div class="tile-btn abs" style="left:124px">
      <svg width="13" height="13" viewBox="0 0 24 24"><path d="M10 14a5 5 0 0 0 7 0l3-3a5 5 0 0 0-7-7l-1 1M14 10a5 5 0 0 0-7 0l-3 3a5 5 0 0 0 7 7l1-1" fill="none" stroke="#e3262c" stroke-width="2.5"/></svg>
    </div>
    <div class="tile-caption abs">Residential Roofing</div>
  </div>
  <div class="tile t4 abs" style="left:851px;top:319px" role="img" aria-label="Two inspectors in hard hats checking a concrete deck"></div>
  <div class="tile t5 abs" style="left:90px;top:536px" role="img" aria-label="Worker raking a thatched roof"></div>
  <div class="tile t6 abs" style="left:344px;top:536px" role="img" aria-label="Roofer in yellow hard hat with nail gun"></div>
  <div class="tile t7 abs" style="left:598px;top:536px" role="img" aria-label="Icicle hanging from a snowy gutter"></div>
  <div class="tile t8 abs" style="left:851px;top:536px" role="img" aria-label="Two workers cutting metal roof sheets"></div>

  <a class="load-more abs">Load More</a>
</main>

<section class="cta abs">
  <p class="cta-kicker abs">Contact Price</p>
  <p class="cta-title abs">Roofing today For a Free Estimate</p>
  <div class="cta-phone abs">
    <svg width="17" height="17" viewBox="0 0 24 24"><path fill="#fff" d="M6.6 10.8a15.1 15.1 0 0 0 6.6 6.6l2.2-2.2c.3-.3.7-.4 1-.2 1.1.4 2.3.6 3.6.6.6 0 1 .4 1 1V20c0 .6-.4 1-1 1A17 17 0 0 1 3 4c0-.6.4-1 1-1h3.5c.6 0 1 .4 1 1 0 1.3.2 2.5.6 3.6.1.3 0 .7-.2 1z"/></svg>
    555-014-0008
  </div>
  <a class="cta-btn abs">REQUEST AN ESTIMATE</a>
</section>

<footer class="footer abs">
  <div class="brand abs"><span class="mark"></span>Brightpeak Roofing</div>
  <div class="footer-phone abs">555-014-0008</div>

  <h3 class="col-title abs" style="left:328px">Quick Links</h3>
  <div class="links">
    <a style="left:330px;top:105px">Home</a>
    <a style="left:330px;top:129px">About Us</a>
    <a style="left:330px;top:153px">Service</a>
    <a style="left:330px;top:176px">Roof Types</a>
    <a style="left:454px;top:105px">Commerical</a>
    <a style="left:454px;top:129px">Residential</a>
    <a style="left:454px;top:153px">Repair</a>
    <a style="left:454px;top:176px">Contact Us</a>
  </div>

  <h3 class="col-title abs" style="left:600px">Contact Info</h3>
  <p class="info abs" style="left:600px;top:104px">Brightpeak Roofing &amp; Construction<br>Company, Inc.</p>
  <div class="info-row abs" style="left:600px;top:151px">
    <svg width="12" height="12" viewBox="0 0 24 24"><path fill="#e3262c" d="M6.6 10.8a15.1 15.1 0 0 0 6.6 6.6l2.2-2.2c.3-.3.7-.4 1-.2 1.1.4 2.3.6 3.6.6.6 0 1 .4 1 1V20c0 .6-.4 1-1 1A17 17 0 0 1 3 4c0-.6.4-1 1-1h3.5c.6 0 1 .4 1 1 0 1.3.2 2.5.6 3.6.1.3 0 .7-.2 1z"/></svg>
    <span>Illinois</span><span style="margin-left:8px">555-014-0008</span>
  </div>
  <div class="info-row abs" style="left:600px;top:175px">
    <svg width="12" height="12" viewBox="0 0 24 24"><path fill="#e3262c" d="M6.6 10.8a15.1 15.1 0 0 0 6.6 6.6l2.2-2.2c.3-.3.7-.4 1-.2 1.1.4 2.3.6 3.6.6.6 0 1 .4 1 1V20c0 .6-.4 1-1 1A17 17 0 0 1 3 4c0-.6.4-1 1-1h3.5c.6 0 1 .4 1 1 0 1.3.2 2.5.6 3.6.1.3 0 .7-.2 1z"/></svg>
    <span>Indiana</span><span style="margin-left:8px">555-019-0018</span>
  </div>

  <div class="social abs" aria-label="Social links"><span>pix</span><span>hum</span><span>orb</span><span>nod</span></div>
  <p class="copyright abs">Copyright 2016<br>Brightpeak Roofing | All Right Reserved</p>
  <div class="pay-badge abs">tillbee</div>

  <div class="chat abs">
    <div class="chat-bubble">
      <svg width="18" height="16" viewBox="0 0 24 22"><path d="M3 2h18v13H9l-5 4v-4H3z" fill="none" stroke="#fff" stroke-width="1.8"/><circle cx="8" cy="8.5" r="1.2" fill="#fff"/><circle cx="12" cy="8.5" r="1.2" fill="#fff"/><circle cx="16" cy="8.5" r="1.2" fill="#fff"/></svg>
    </div>
    <div class="chat-label"><small>Live</small><b>Chat</b></div>
  </div>
</footer>

</body>
</html>
```